Strong, modern, clean Business Card design

Looking for a stunning, but CLEAN business card design. While we are a faith-based organization, we do NOT want this to look religious.

Industry/Entity Type

Non-Profit

Contact Information for Business Card

Dale Munroe | Lead Pastor
dale@BrightHarvestHope.org
970-555-0148
PO Box 7316
Loveland, CO 80571

Font styles to use
Serif
Sans Serif

Requirements
Should not have
• Religious imagery or symbolism

```html
<!DOCTYPE html>
<html lang="en">
<head>
<meta charset="utf-8">
<title>Harvest Point Church — Business Card</title>
<link rel="stylesheet" href="https://fonts.googleapis.com/css2?family=Lato:wght@400;700&display=swap">
<style>
  :root {
    --page-bg: #d9dde2;
    --card-bg: #020202;
    --band: #557e93;
    --white: #ffffff;
    --text-light: #f2f2f2;
    --icon: #5d8aa0;
  }
  * { margin: 0; padding: 0; box-sizing: border-box; }
  html, body {
    width: 1200px; height: 809px; overflow: hidden;
    background: var(--page-bg);
  }
  .card {
    position: absolute;
    left: 150px; top: 148px;
    width: 899px; height: 513px;
    background: var(--card-bg);
    border-radius: 40px;
    overflow: hidden;
    font-family: "Lato", Arial, sans-serif;
    color: var(--text-light);
  }
  .org-name {
    position: absolute; left: 53px; top: 64px;
    font-weight: 700; font-size: 40px; line-height: 1;
    color: var(--white); text-transform: uppercase;
    white-space: nowrap;
  }
  .title-band {
    position: absolute; left: 0; top: 199px; width: 100%; height: 69px;
    background: var(--band);
  }
  .person-name {
    position: absolute; left: 53px; top: 50%; transform: translateY(-50%);
    font-weight: 700; font-size: 30px; line-height: 1;
    color: var(--white); text-transform: uppercase;
  }
  .divider {
    position: absolute; left: 315px; top: 22px;
    width: 2px; height: 26px; background: var(--text-light);
  }
  .role {
    position: absolute; left: 354px; top: 50%; transform: translateY(-50%);
    font-size: 20px; line-height: 1; color: var(--white);
  }
  .address {
    position: absolute; left: 53px; top: 296px;
    font-style: normal; font-size: 20px; line-height: 27px;
  }
  .contact-list {
    position: absolute; left: 62px; top: 394px; list-style: none;
    font-size: 20px;
  }
  .contact-list li {
    display: flex; align-items: center; height: 28px; margin-bottom: 11px;
  }
  .contact-list svg { width: 16px; height: 16px; margin-right: 12px; fill: var(--icon); }
</style>
</head>
<body>
  <div class="card">
    <div class="org-name">Harvest Point Church</div>

    <div class="title-band">
      <span class="person-name">Dale Munroe</span>
      <span class="divider"></span>
      <span class="role">Lead Pastor</span>
    </div>

    <address class="address">
      PO Box 7316<br>
      Loveland, CO 80571
    </address>

    <ul class="contact-list">
      <li>
        <svg viewBox="0 0 24 24" aria-hidden="true"><path d="M6.6 10.8a15.1 15.1 0 0 0 6.6 6.6l2.2-2.2c.3-.3.7-.4 1-.2 1.1.4 2.3.6 3.6.6.6 0 1 .4 1 1V20c0 .6-.4 1-1 1A17 17 0 0 1 3 4c0-.6.4-1 1-1h3.5c.6 0 1 .4 1 1 0 1.3.2 2.5.6 3.6.1.3 0 .7-.2 1z"/></svg>
        <span>970-555-0148</span>
      </li>
      <li>
        <svg viewBox="0 0 24 24" aria-hidden="true"><path d="M2 5h20v14H2z"/><path d="M2 5l10 8 10-8" fill="none" stroke="#020202" stroke-width="1.8"/></svg>
        <span>dale@BrightHarvestHope.org</span>
      </li>
    </ul>
  </div>
</body>
</html>
```